PPT Template for a company that develops software and intellectual property for use by accountants a

We are a boutique firm that develops specialised reporting applications, financial and non-financial reporting content, checklists and other intellectual property for use by business consultants and accounting firms in particular. The applications and content we are creating is strategically focussed and we are required to produce reports and presentations and our current templates are simply not sufficient.

Excel worksheets, graphs and other graphics are regularly embedded into the presentations
We have our logo in 4 colour palettes and will require the winning version to be provided in all 4 colours plus B&W. There is one single logo but the name “Harbor Ledger Pathfinders” is presented in 3 different styles for use depending on the space available etc.
Our clients will typically take our products and rebrand/co brand these (we require them to at least say that there product is “powered by Harbor Ledger Pathfinders” with the logo.
The templates you provide will be used to create marketing presentations, proposal presentations and our standard documents that clients will rebrand or cobrand under license.

A Powerpoint Document Slide Template

Cover page layout, back page, intermediate page heading, in colours and styles based on the logo, title styles, and an intermediate or chapter heading slide style. Many of our presentations contain slides with tables, diagrams, flowcharts and text, including simple lists of bullet points. As above, you will see in our style guide that we have four coloured logos – we would like one version in each. We recommend that we finalise the design using the maroon version and then this be used as the base for the other colour palettes.
Again, the cover should be bold and draw attention but remain professional.

We are looking for something that works in both 4:3 and 16:9 (or two templates please)

We like a clear professional and simple look.

Deliverable: PowerPoint template file (.potx extension) for PowerPoint 2007 with at least a “cover” layout, a “title and content” layout, and a simplified slide layout, as well as “back cover”. Please embed any fonts used.

Industry/Entity Type

Financial

```html
<!DOCTYPE html>
<html lang="en">
<head>
<meta charset="utf-8">
<title>Project Title Here — Harbor Ledger Pathfinders</title>
<link rel="stylesheet" href="https://fonts.googleapis.com/css2?family=Open+Sans:wght@400;600;700&display=swap">
<style>
  :root {
    --brand-orange: #f26f21;
    --title-grey: #4a4a4a;
    --text-dark: #2f2f2f;
    --paper: #ffffff;
    --photo-paper: #f7f8f9;
    --photo-shade: #c9ced3;
    --photo-green: #b8d35a;
    --photo-blue: #8fc3e4;
    --photo-amber: #f0b24a;
    --photo-skin: #e8c9b6;
  }
  * { margin: 0; padding: 0; box-sizing: border-box; }
  html, body {
    width: 1200px;
    height: 900px;
    overflow: hidden;
    background: var(--paper);
  }
  .cover-slide {
    position: relative;
    width: 1200px;
    height: 900px;
    background: var(--paper);
    font-family: "Open Sans", Arial, sans-serif;
    overflow: hidden;
  }
  .hero-photo {
    position: absolute;
    left: 0;
    top: 0;
    width: 1200px;
    height: 582px;
    background:
      radial-gradient(ellipse 300px 180px at 660px 90px, rgba(143,195,228,0.85) 0%, rgba(184,211,90,0.7) 45%, transparent 100%),
      radial-gradient(ellipse 260px 140px at 270px 150px, rgba(184,211,90,0.55) 0%, transparent 100%),
      radial-gradient(ellipse 200px 120px at 690px 450px, rgba(240,178,74,0.6) 0%, transparent 100%),
      radial-gradient(ellipse 180px 200px at 220px 300px, rgba(201,206,211,0.9) 0%, transparent 100%),
      radial-gradient(ellipse 150px 220px at 130px 480px, rgba(232,201,182,0.8) 0%, transparent 100%),
      radial-gradient(ellipse 150px 260px at 980px 200px, rgba(232,201,182,0.75) 0%, transparent 100%),
      linear-gradient(165deg, #e4e7ea 0%, var(--photo-paper) 45%, #eceef0 100%);
  }
  .company-name {
    position: absolute;
    left: 64px;
    top: 798px;
    display: flex;
    align-items: center;
    gap: 12px;
    font-size: 30px;
    font-weight: 400;
    color: var(--text-dark);
    white-space: nowrap;
  }
  .company-dot {
    width: 18px;
    height: 18px;
    border-radius: 50%;
    background: var(--brand-orange);
  }
  .title-block {
    position: absolute;
    right: 15px;
    top: 664px;
    width: 560px;
    text-align: right;
  }
  .project-title {
    font-size: 54px;
    font-weight: 600;
    line-height: 1.1;
    color: var(--title-grey);
    letter-spacing: -0.5px;
    white-space: nowrap;
  }
  .project-title .accent { color: var(--brand-orange); }
  .project-subtext {
    margin-top: 20px;
    font-size: 21px;
    font-weight: 600;
    line-height: 29px;
    color: var(--text-dark);
    white-space: nowrap;
  }
  .footer-band {
    position: absolute;
    left: 0;
    bottom: 0;
    width: 1200px;
    height: 30px;
    background: var(--brand-orange);
  }
</style>
</head>
<body>
  <main class="cover-slide">
    <div class="hero-photo" role="img" aria-label="Photograph of hands using a calculator and pen over printed financial reports with bar and pie charts"></div>

    <div class="company-name">
      <span class="company-dot"></span>
      <span>Harbor Ledger Pathfinders</span>
    </div>

    <div class="title-block">
      <h1 class="project-title"><span class="accent">Project</span> TItle Here</h1>
      <p class="project-subtext">Subtext here&nbsp; Subtext here Subtext here<br>Subtext here Subtext here Subtext here Subtext<br>here&nbsp; Subtext here</p>
    </div>

    <div class="footer-band"></div>
  </main>
</body>
</html>
```